Real Estate Card Design

I need a new business card! Below you will find my headshot, the company logo and a copy of my previous business card.

The card must contain the following information:

Dana Welch
Sales Representative
FAIR HARBOUR HOMES REALTY INC BROKERGE
204-517 Maple Ave E, Oshawa ON L1G 4K7
Cell: 905-618-4037 Office:905-481-2696
www.danawelch.com dana@movewithwelch.ca

I would like the card to portray security and class all the while being fresh and contemporary. I hold the key....

```html
<!DOCTYPE html>
<html lang="en">
<head>
<meta charset="utf-8">
<title>Dana Welch – Business Card</title>
<link href="https://fonts.googleapis.com/css2?family=Fira+Sans+Condensed:wght@400;600&display=swap" rel="stylesheet">
<style>
  :root {
    --backdrop: #808080;
    --card: #ffffff;
    --brand-blue: #2fa6e0;
    --ink: #1d1d1f;
    --suit-dark: #1c2433;
    --suit-mid: #3d4a5e;
    --skin-light: #d9b79c;
  }
  * { margin: 0; padding: 0; box-sizing: border-box; }
  html, body { width: 1200px; height: 900px; overflow: hidden; }
  body {
    background: var(--backdrop);
    font-family: "Fira Sans Condensed", "Arial Narrow", sans-serif;
    color: var(--ink);
    display: flex; align-items: center; justify-content: center;
  }
  .business-card {
    position: relative;
    width: 840px; height: 480px;
    background: var(--card);
    border-radius: 28px;
    overflow: hidden;
  }
  .card-shapes { position: absolute; inset: 0; width: 100%; height: 100%; }

  .brand {
    position: absolute; left: 150px; top: 34px;
    display: flex; align-items: center; gap: 14px;
  }
  .brand-name {
    font-weight: 600; font-size: 21px; line-height: 1.05;
    letter-spacing: 0.5px; color: var(--ink); text-transform: uppercase;
    text-align: right;
  }
  .brand-square { width: 86px; height: 86px; background: var(--brand-blue); }

  .agent { position: absolute; left: 44px; top: 150px; }
  .agent-name {
    font-weight: 600; font-size: 38px; color: var(--brand-blue);
    text-transform: uppercase; letter-spacing: 0.5px; line-height: 1;
  }
  .agent-title { font-size: 20px; margin-top: 6px; }

  .contact { position: absolute; left: 44px; top: 252px; font-size: 21px; line-height: 1.55; }
  .contact .label { color: var(--brand-blue); }
  .contact .gap { display: inline-block; width: 20px; }

  .address {
    position: absolute; left: 44px; bottom: 14px;
    font-size: 21px; color: #fff; letter-spacing: 0.3px;
  }
</style>
</head>
<body>
  <div class="business-card">
    <svg class="card-shapes" viewBox="0 0 840 480" aria-hidden="false">
      <line class="rule-brand" x1="60" y1="132" x2="420" y2="132" stroke="var(--brand-blue)" stroke-width="2"/>
      <line class="rule-name" x1="44" y1="236" x2="560" y2="236" stroke="var(--brand-blue)" stroke-width="2"/>
      <path class="address-band" d="M0,422 L560,422 L560,480 L0,480 Z" fill="var(--brand-blue)"/>
      <defs>
        <linearGradient id="portraitTone" x1="0" y1="1" x2="1" y2="0">
          <stop offset="0" stop-color="var(--suit-dark)"/>
          <stop offset="0.6" stop-color="var(--suit-mid)"/>
          <stop offset="1" stop-color="var(--skin-light)"/>
        </linearGradient>
      </defs>
      <path class="agent-portrait" role="img" aria-label="Portrait of the agent in a dark pinstripe suit holding up a house key"
        d="M450,480 C520,468 560,420 590,380 C620,330 650,300 700,290 C720,230 760,190 820,200 L840,205 L840,480 Z"
        fill="url(#portraitTone)"/>
    </svg>

    <div class="brand">
      <div class="brand-name">Fair Harbour Homes<br>Realty Inc. Brokerge</div>
      <div class="brand-square"></div>
    </div>

    <div class="agent">
      <div class="agent-name">Dana Welch</div>
      <div class="agent-title">Sales Representative</div>
    </div>

    <div class="contact">
      <div><span class="label">Cell:</span> 905-618-4037<span class="gap"></span><span class="label">Office:</span> 905-481-2696</div>
      <div><span class="label">Web:</span> www.danawelch.com<span class="gap"></span><span class="label">Email:</span> dana@movewithwelch.ca</div>
    </div>

    <div class="address">204-517 Maple Ave E, Oshawa ON L1G 4K7</div>
  </div>
</body>
</html>
```